Office Building Banner

Need a 4x8 vinyl banner made for our office/storage headquarters. Our branded colors and logo can be taken from our website, www.halvenroofingtx.com. All other elements of our brand have not been decided on yet, so you have creative autonomy there. Our location faces a busy highway in Seguin, Texas, so the banner needs to have our contact information and full name clearly seen from a bit away's away, hope that makes sense. Our company wants to convey attributes of strength, loyalty, protection - basically emulating the qualities of a wolf and his pack. I have uploaded a few items we have been using to date, but as you can see, graphic design is not our forte.

```html
<!DOCTYPE html>
<html lang="en">
<head>
<meta charset="UTF-8">
<title>Halven Roofing &amp; Renovation – Banner</title>
<link href="https://fonts.googleapis.com/css2?family=Poppins:wght@400;600;700;800&family=Oswald:wght@500&display=swap" rel="stylesheet">
<style>
  :root {
    --banner-black: #000000;
    --brand-orange: #ff8210;
    --text-white: #ffffff;
    --icon-black: #0a0a0a;
    --photo-roof: #7d6257;
    --photo-siding: #6b675f;
    --photo-trim: #d8cfbf;
  }
  html, body {
    margin: 0;
    padding: 0;
    width: 1200px;
    height: 2400px;
    overflow: hidden;
    background: var(--banner-black);
  }
  .banner {
    position: relative;
    width: 1200px;
    height: 2400px;
    background: var(--banner-black);
    font-family: 'Poppins', sans-serif;
    color: var(--text-white);
    overflow: hidden;
  }
  .brand-mark {
    position: absolute;
    top: 170px;
    left: 0;
    width: 1200px;
    display: flex;
    justify-content: center;
    align-items: center;
    gap: 26px;
  }
  .brand-mark__circle {
    width: 150px;
    height: 150px;
    border: 8px solid var(--text-white);
    border-radius: 50%;
    box-sizing: border-box;
  }
  .brand-mark__name {
    font-weight: 700;
    font-size: 84px;
    letter-spacing: 2px;
    line-height: 1;
    color: var(--text-white);
  }
  .headline {
    position: absolute;
    top: 585px;
    left: 0;
    width: 1200px;
    text-align: center;
    margin: 0;
  }
  .headline__name {
    display: block;
    font-weight: 800;
    font-size: 192px;
    line-height: 1;
    letter-spacing: -4px;
    color: var(--brand-orange);
  }
  .headline__service {
    display: block;
    font-weight: 700;
    font-size: 160px;
    line-height: 1;
    letter-spacing: -1px;
    color: var(--text-white);
    margin-top: 22px;
  }
  .headline__service + .headline__service {
    margin-top: 2px;
  }
  .house-photo {
    position: absolute;
    top: 1120px;
    left: 0;
    width: 1200px;
    height: 860px;
    background: linear-gradient(180deg,
      #000000 0%,
      #1c1c1e 14%,
      var(--photo-roof) 36%,
      var(--photo-siding) 58%,
      var(--photo-trim) 78%,
      #5a5a4e 100%);
  }
  .contact-band {
    position: absolute;
    left: 0;
    top: 1840px;
    width: 1200px;
    height: 560px;
  }
  .contact-band svg {
    display: block;
  }
  .phone {
    position: absolute;
    top: 2025px;
    left: 0;
    width: 1200px;
    display: flex;
    justify-content: center;
    align-items: center;
    gap: 30px;
  }
  .phone__icon {
    width: 134px;
    height: 134px;
  }
  .phone__number {
    font-family: 'Oswald', sans-serif;
    font-weight: 500;
    font-size: 172px;
    line-height: 1;
    letter-spacing: 2px;
    color: var(--text-white);
  }
  .website {
    position: absolute;
    top: 2222px;
    left: 0;
    width: 1200px;
    text-align: center;
    font-size: 66px;
    font-weight: 400;
    color: var(--text-white);
    line-height: 1;
  }
  .website__domain {
    font-weight: 700;
    color: var(--icon-black);
  }
</style>
</head>
<body>
  <main class="banner">
    <div class="brand-mark">
      <span class="brand-mark__circle"></span>
      <span class="brand-mark__name">HALVEN</span>
    </div>

    <h1 class="headline">
      <span class="headline__name">HALVEN</span>
      <span class="headline__service">ROOFING &amp;</span>
      <span class="headline__service">RENOVATION</span>
    </h1>

    <div class="house-photo" role="img" aria-label="Photograph of a large two-storey suburban house with brown shingle roof, grey siding and white trim"></div>

    <div class="contact-band">
      <svg width="1200" height="560" viewBox="0 0 1200 560" aria-hidden="true">
        <path d="M0 0 C 60 90, 250 100, 520 70 C 780 40, 1000 30, 1200 70 L1200 560 L0 560 Z" fill="#ffffff"/>
        <path d="M0 60 C 120 130, 330 110, 560 88 C 800 66, 1030 70, 1200 110 L1200 560 L0 560 Z" fill="var(--brand-orange)"/>
      </svg>
    </div>

    <div class="phone">
      <svg class="phone__icon" viewBox="0 0 134 134" aria-hidden="true">
        <circle cx="67" cy="67" r="67" fill="var(--icon-black)"/>
        <path d="M48 34 l12 -4 l10 22 l-10 8 c4 12 12 20 24 24 l8 -10 l22 10 l-4 12 c-2 6 -8 8 -14 6 c-30 -8 -50 -28 -56 -56 c-2 -6 2 -10 8 -12 z" fill="var(--brand-orange)"/>
      </svg>
      <span class="phone__number">512-555-0148</span>
    </div>

    <p class="website" style="margin:0">www.<span class="website__domain">halvenroofingtx</span>.com</p>
  </main>
</body>
</html>
```